Doctor in Veterinary Medecine/ veterinarian

I am a vet and would like a buisness card which is simple yet elegant and professional.
My aim is to help as much animals as I can. My main field of expertise are dogs and cats. I would like the card to reflect a "family doctor" feeling.
It should not be the traditional picture of a paw or a dog but yet it should have a sign of a pet on it. I would like to have my name Lina Haddour as well as my profession D.V.M and my number.

Target Market(s)

Lebanese population who have pets

Industry/Entity Type

Doctor

Contact Information for Business Card

Should contain my profession " D.V.M", my full name "Lina Haddour" and my number "0096171552934"

Requirements
Must have
• A certain picture depicting my profession
Nice to have
• Some sort of picture related to pets and animals
Should not have
• A picture of a paw or a dog. I need something more creative

```html
<!DOCTYPE html>
<html lang="en">
<head>
<meta charset="utf-8">
<title>Lina Haddour D.V.M. – Business Card</title>
<link rel="stylesheet" href="https://fonts.googleapis.com/css2?family=Cinzel:wght@600;700&family=Open+Sans:wght@400&display=swap">
<style>
  :root {
    --page-bg: #eeeeef;
    --card-bg: #f8f8f8;
    --brand-blue: #1a5aa8;
    --navy: #283891;
    --sky: #00aeef;
    --leaf: #3bb44a;
    --text-grey: #7a7a7a;
    --rule-grey: #a8a8a8;
  }
  * { box-sizing: border-box; margin: 0; padding: 0; }
  html, body {
    width: 1200px;
    height: 970px;
    overflow: hidden;
    background: var(--page-bg);
  }
  .business-card {
    position: absolute;
    left: 80px;
    top: 168px;
    width: 1040px;
    height: 634px;
    background: var(--card-bg);
    border-radius: 37px;
    overflow: hidden;
  }
  .base-band {
    position: absolute;
    left: 0;
    bottom: 0;
    width: 100%;
    height: 190px;
  }
  .practice-name {
    position: absolute;
    left: 745px;
    top: 165px;
    width: 230px;
    font-family: "Cinzel", serif;
    font-weight: 600;
    font-size: 28px;
    line-height: 1.25;
    color: var(--brand-blue);
    text-align: center;
  }
  .practice-name::after {
    content: "";
    display: block;
    width: 220px;
    height: 6px;
    margin: 18px auto 0;
    border-radius: 50%;
    background: var(--brand-blue);
  }
  .doctor-name {
    position: absolute;
    left: 86px;
    top: 258px;
    font-family: "Cinzel", serif;
    font-weight: 700;
    font-size: 40px;
    letter-spacing: -1px;
    color: var(--brand-blue);
    white-space: nowrap;
  }
  .doctor-name .credential {
    font-family: "Open Sans", sans-serif;
    font-weight: 400;
    font-size: 24px;
    letter-spacing: 0.5px;
    color: var(--text-grey);
    margin-left: 10px;
  }
  .contact-row {
    position: absolute;
    left: 89px;
    display: flex;
    align-items: center;
    gap: 24px;
  }
  .contact-row.phone { top: 356px; }
  .contact-row.hours { top: 410px; }
  .contact-icon {
    width: 43px;
    height: 43px;
    border-radius: 6px;
    background: var(--brand-blue);
    display: flex;
    align-items: center;
    justify-content: center;
  }
  .contact-text {
    font-family: "Open Sans", sans-serif;
    font-size: 32px;
    color: var(--text-grey);
  }
  .hours-line {
    width: 695px;
    margin-top: 30px;
    border-top: 2px dotted var(--rule-grey);
  }
</style>
</head>
<body>
  <div class="business-card">
    <svg class="base-band" viewBox="0 0 1040 190" preserveAspectRatio="none" role="img" aria-label="Decorative wave band in green and blue">
      <defs>
        <linearGradient id="bandFill" x1="0" y1="0" x2="1" y2="0">
          <stop offset="0" stop-color="#3bb44a"/>
          <stop offset="0.35" stop-color="#00aeef"/>
          <stop offset="1" stop-color="#283891"/>
        </linearGradient>
      </defs>
      <path d="M0,110 Q560,150 1040,10 L1040,190 L0,190 Z" fill="url(#bandFill)"/>
    </svg>

    <div class="practice-name">Haddour Pet&nbsp;Care</div>

    <h1 class="doctor-name">Dr. Lina Haddour<span class="credential">D.V.M.</span></h1>

    <div class="contact-row phone">
      <span class="contact-icon">
        <svg width="26" height="26" viewBox="0 0 24 24" aria-hidden="true">
          <path fill="#ffffff" d="M6.6 2.5c.5-.3 1.1-.1 1.4.4l1.8 3.3c.3.5.1 1.1-.3 1.4L8.2 8.4c-.3.2-.4.6-.3.9.8 2.4 2.3 5 4.2 6.8.3.3.7.3 1 .1l1.3-.9c.5-.3 1.1-.2 1.4.3l2.1 3.1c.3.5.2 1.1-.3 1.4l-1.7 1.1c-.9.6-2.1.7-3 .1C8.4 18.6 5.2 13.6 4.4 8.3c-.2-1.1.3-2.2 1.2-2.8z"/>
        </svg>
      </span>
      <span class="contact-text">00961-71-552934</span>
    </div>

    <div class="contact-row hours">
      <span class="contact-icon">
        <svg width="30" height="30" viewBox="0 0 24 24" aria-hidden="true">
          <circle cx="12" cy="12" r="9.5" fill="none" stroke="#ffffff" stroke-width="2"/>
          <path d="M12 6.5V12h4.5" fill="none" stroke="#ffffff" stroke-width="2" stroke-linecap="round"/>
        </svg>
      </span>
      <span class="hours-line" aria-label="Opening hours"></span>
    </div>
  </div>
</body>
</html>
```